Brookvale Insurance Services - Insurance Agency Wesbite

I need a website for my insurance agency called Brookvale Insurance Services. I have attached my company logo. You can use the colors from the copy logo to create the website color scheme. I need a Request A Quote section.
Business Address: 7816 Marlowe Ave Unit D, Studio City Ca 91627
Business Phone: (818) 555-0193
I would need the following drop downs on the main page:

1st drop down:
Business Insurance
⁃ Commercial Auto
⁃ Employment Practice Liability Insurance
⁃ General Liability Insurance
⁃ Professional Liability Insurance
⁃ Property Insurance
⁃ Workers Compensation Insurance

2nd drop down:
Industries We Serve
- Construction
- Janitorial
- Landscapers
- Trucking
- ParcelRun Independent Service Providers (ISP)
Healthcare Industry
- Community Care Facilities
- Home Health Agencies
- Hospice
- Nursing Homes

3rd drop down:
Risk Management
- Claims Management
- Compliance & Risk Management

4th drop down
Request a quote

5th drop down
About Us

6th drop down
Contact US

Target Market(s)

Potential clients

Industry/Entity Type

Business Insurance

Coding

Coded - Design and coding required

Number of Pages Required

5+ page

Colors
0054AA
0677BA
7BADD7
CADEEF
E8F1F8
00AB8E
00BBA5
67D7C9
C6EFE9
E9F9F6

Requirements
Must have
• Home Business Insurance - Commercial Auto - Employment Practice Liability Insurance - General Liability Insurance - Professional Liability Insurance - Property Insurance - Workers Compensation Insurance Industries We Serve - Construction - Janitorial - Landscapers - Manufacturing Companies - Restaurants - Towing - Trucking Healthcare Industry - Community Care Facilities - Home Health Agencies - Hospice - Nursing Homes - Risk Management - Claims Management - Compliance & Risk Management Request a Quote About Us Contact Us

```html
<!DOCTYPE html>
<html lang="en">
<head>
<meta charset="utf-8">
<title>Brookvale Insurance Services</title>
<link href="https://fonts.googleapis.com/css2?family=Lexend:wght@300;400;500;600&family=Poppins:wght@400;500;600&display=swap" rel="stylesheet">
<style>
:root{
  --green:#2a9a47;
  --navy:#1d2142;
  --ink:#15152d;
  --text:#222;
  --muted:#555;
  --grey-bg:#e8e8e8;
  --line:#cfcfcf;
  --white:#fff;
}
*{box-sizing:border-box;margin:0;padding:0}
html,body{width:1200px;height:4766px;overflow:hidden}
body{font-family:"Poppins",sans-serif;color:var(--text);background:var(--white);position:relative}
h1,h2,h3{font-family:"Lexend",sans-serif;font-weight:400;color:var(--ink)}
.abs{position:absolute}
section,header,footer{position:relative;width:1200px}
.btn{display:inline-block;background:var(--green);color:#fff;font-size:12px;font-weight:500;text-transform:uppercase;text-align:center;letter-spacing:.3px}
.photo{position:absolute}

/* header */
.site-header{height:62px;background:#fff}
.brand{left:115px;top:18px;font-family:"Lexend",sans-serif;font-weight:600;font-size:17px;color:var(--navy);display:flex;align-items:center;gap:6px}
.brand .dot{width:9px;height:9px;background:var(--green)}
.brand small{display:block;font-size:7px;letter-spacing:2px;color:var(--green);font-weight:600}
.main-nav{left:352px;top:24px;display:flex;gap:20px;font-size:11.5px}
.main-nav span::after{content:" \2304";font-size:9px}
.main-nav span.plain::after{content:""}
.nav-quote{left:851px;top:12px;width:129px;height:34px;border:1px solid #999;font-size:10px;line-height:32px;text-align:center;color:#333}
.nav-contact{left:988px;top:12px;width:101px;height:34px;line-height:34px;font-size:10px}

/* hero */
.hero{height:570px;overflow:hidden}
.hero-bg{inset:0;background:linear-gradient(100deg,#17202a 0%,#2d3b3a 35%,#4d5f52 55%,#3a4a3e 75%,#20271f 100%)}
.hero h1{left:108px;top:142px;font-size:40px;line-height:47px;color:#fff;font-weight:400;width:420px}
.hero-copy{left:112px;top:293px;width:380px;font-size:12.5px;line-height:19px;color:#e8e8e8;border-left:2px solid var(--green);padding-left:8px}
.hero .btn{left:111px;top:378px;width:154px;height:43px;line-height:43px}
.follow{left:34px;top:200px;display:flex;flex-direction:column;align-items:center;gap:12px}
.follow i{display:block;width:9px;height:9px;border-radius:50%;background:#fff}
.follow .rule{width:1px;height:60px;background:#aaa}
.follow b{font-weight:400;font-size:11px;color:#fff;writing-mode:vertical-rl;transform:rotate(180deg)}
.hero-phone{left:1132px;top:150px;display:flex;flex-direction:column;align-items:center;gap:12px}
.hero-phone b{font-weight:400;font-size:11px;color:#fff;writing-mode:vertical-rl}
.hero-phone .rule{width:1px;height:80px;background:#aaa}
.scroll-tab{left:580px;top:548px;width:40px;height:22px;background:#fff;border-radius:20px 20px 0 0}
.scroll-tab i{position:absolute;left:16px;top:8px;width:8px;height:12px;border:1px solid #333;border-radius:4px}

/* business */
.business{height:531px}
.section-title{position:absolute;left:0;width:1200px;text-align:center;font-size:33px}
.business .section-title{top:136px}
.tree{left:0;top:0;width:1200px;height:531px}
.cover{position:absolute;width:140px;text-align:center;top:300px;font-family:"Lexend",sans-serif;font-size:13px;line-height:18px;color:var(--ink);font-weight:500}
.cover .ring{width:74px;height:74px;border-radius:50%;background:#e6e6e6;margin:0 auto 13px;display:flex;align-items:center;justify-content:center}
.cover .ring i{width:30px;height:30px;border:2px solid #444;border-radius:6px}
.cover.active .ring{background:var(--navy)}
.cover.active .ring i{border-color:var(--green)}

/* industries */
.industries{height:500px;background:var(--grey-bg);overflow:hidden}
.industries .photo{left:166px;top:22px;width:390px;height:478px;background:linear-gradient(180deg,#d9d9d9,#3b3b40 60%,#2b2b30)}
.ind-accent{left:0;top:330px;width:1200px;height:170px}
.industries h2{position:absolute;left:618px;top:82px;font-size:33px}
.ind-tab{left:618px;top:137px;width:182px;height:48px;background:#fff;box-shadow:0 2px 8px rgba(0,0,0,.12)}
.ind-tab::after{content:"";position:absolute;right:14px;top:17px;width:14px;height:14px;border-radius:50%;background:#ccc}
.ind-list li{position:absolute;list-style:none;font-size:13.5px;color:var(--ink);padding-left:20px}
.ind-list li::before{content:"";position:absolute;left:0;top:8px;width:5px;height:5px;border-radius:50%;background:var(--ink)}
.ind-list li.first::before{background:var(--green)}
.ind-head{left:618px;top:282px;font-family:"Lexend",sans-serif;font-size:14px;color:#aaa}

/* risk */
.risk{height:1100px}
.risk .section-title{top:127px}
.risk-block{position:absolute;width:360px;text-align:center}
.risk-block .badge{width:58px;height:58px;border-radius:50%;background:#fff;box-shadow:0 2px 8px rgba(0,0,0,.15);margin:0 auto 20px;display:flex;align-items:center;justify-content:center}
.risk-block .badge i{width:22px;height:22px;border:2px solid #444;border-radius:50%}
.risk-block h3{font-size:21px;font-weight:500;margin-bottom:16px;line-height:26px}
.risk-block p{font-size:12.5px;line-height:18px;color:var(--muted)}
.risk-block .more{width:24px;height:24px;border-radius:50%;background:#ddd;margin:25px auto 0;font-size:12px;line-height:24px;color:#444}
.green-corner{position:absolute;background:var(--green)}

/* quote */
.quote{height:375px;background:var(--navy);overflow:hidden}
.quote .photo{left:610px;top:0;width:590px;height:375px;background:linear-gradient(90deg,#1d2142 0%,#4a4e60 30%,#7a7b80 60%,#5c5d66)}
.quote h2{position:absolute;left:168px;top:100px;font-size:34px;color:#fff}
.quote p{position:absolute;left:168px;top:157px;width:420px;font-size:12px;line-height:18px;color:#ddd}
.quote .field{left:170px;top:210px;width:420px;height:39px;background:#fff;font-size:11px;color:#999;padding:12px 20px}
.quote .btn{left:170px;top:261px;width:121px;height:37px;line-height:37px;font-size:11px}

/* about */
.about{height:615px}
.about .back{left:120px;top:114px;width:240px;height:346px;background:linear-gradient(160deg,#c9b9a8,#6d6d78)}
.about .front{left:276px;top:212px;width:284px;height:339px;background:linear-gradient(160deg,#ebe3d8,#b78a6a 55%,#5a4b46);outline:6px solid #fff}
.about h2{position:absolute;left:618px;top:145px;font-size:34px}
.about .copy{left:618px;top:200px;width:464px;font-size:12.5px;line-height:18px;color:#444}
.about .copy p+p{margin-top:18px}
.about .btn{left:620px;top:490px;width:154px;height:42px;line-height:42px}

/* contact */
.contact{height:1013px}
.dark-band{left:0;top:440px;width:1200px;height:573px;background:var(--ink)}
.contact .section-title{top:64px}
.contact .sub{position:absolute;left:0;width:1200px;top:118px;text-align:center;font-size:12.5px;color:#444}
.contact .photo{left:148px;top:162px;width:484px;height:444px;background:linear-gradient(150deg,#e8e8ea,#9ea3ab 45%,#3e4048)}
.form-card{left:529px;top:209px;width:482px;height:345px;background:#fff;box-shadow:0 4px 18px rgba(0,0,0,.12);padding:36px 45px}
.form-card h3{font-size:19px;font-weight:500;margin-bottom:20px}
.form-card .row{display:flex;gap:8px;margin-bottom:17px}
.form-card .in{flex:1;height:41px;border:1px solid var(--line);font-size:9px;padding:13px 15px;text-transform:uppercase;color:#333}
.form-card .msg{height:75px}
.form-card .btn{width:137px;height:38px;line-height:38px;margin-top:10px}

.footer-brand{left:123px;top:3592px;font-family:"Lexend",sans-serif;font-size:26px;font-weight:600;color:#3048a8;display:flex;align-items:center;gap:8px}
.footer-brand .dot{width:12px;height:12px;background:var(--green)}
.footer-tag{left:124px;top:3628px;font-size:10px;letter-spacing:3px;color:var(--green)}
.footer-about{left:125px;top:3655px;width:260px;font-size:13px;line-height:20px;color:#ddd}
.footer-social{left:125px;top:3752px;display:flex;gap:10px}
.footer-social i{width:22px;height:22px;border-radius:50%;border:1px solid #888}
.site-footer{position:absolute;left:0;top:0;width:1200px;height:4766px;pointer-events:none}
.fcol{position:absolute;color:#ddd;font-size:12px}
.fcol h4{font-family:"Lexend",sans-serif;font-weight:500;font-size:14px;color:#fff;margin-bottom:20px}
.fcol li{list-style:none;line-height:27px}
.fcol li::before{content:"\00BB  ";color:#aaa}
.contact-item{display:flex;gap:10px;margin-bottom:15px;line-height:16px}
.contact-item svg{flex:none;margin-top:2px}
.contact-item b{display:block;color:#fff;font-weight:500;font-size:13px}
.news-input{width:200px;height:34px;background:#fff;font-size:9px;color:#999;padding:11px 20px}
.news-btn{width:126px;height:34px;line-height:34px;margin-top:10px}
.copyright{left:96px;top:4736px;font-size:11.5px;color:#ddd}
.terms{left:910px;top:4736px;font-size:11.5px;color:#ddd}
</style>
</head>
<body>

<header class="site-header">
  <div class="abs brand"><span class="dot"></span><span>BROOKVALE<small>INSURANCE SERVICES</small></span></div>
  <nav class="abs main-nav">
    <span>Business Insurance</span><span>Industries We Serve</span><span>Risk Management</span><span class="plain">About Us</span>
  </nav>
  <div class="abs nav-quote">REQUEST A QUOTE</div>
  <div class="abs nav-contact btn">CONTACT US</div>
</header>

<section class="hero">
  <div class="abs hero-bg" role="img" aria-label="Man working on a laptop outdoors above a misty mountain valley"></div>
  <h1 class="abs">Providing Top-Tier Insurance Products And Resources</h1>
  <p class="abs hero-copy">Brookvale Insurance Services stands as a full service insurance brokerage committed to unparalleled service and exceptional value.</p>
  <span class="abs btn">Get Started</span>
  <div class="abs follow"><i></i><i></i><i></i><i></i><span class="rule"></span><b>Follow Us :</b></div>
  <div class="abs hero-phone"><b>(818) 555-0193</b><span class="rule"></span>
    <svg width="12" height="12" viewBox="0 0 24 24"><path fill="#fff" d="M6.6 10.8a15 15 0 0 0 6.6 6.6l2.2-2.2c.3-.3.7-.4 1-.2 1.1.4 2.3.6 3.6.6.6 0 1 .4 1 1V20c0 .6-.4 1-1 1A17 17 0 0 1 3 4c0-.6.4-1 1-1h3.5c.6 0 1 .4 1 1 0 1.3.2 2.5.6 3.6.1.3 0 .7-.2 1z"/></svg>
  </div>
  <div class="abs scroll-tab"><i></i></div>
</section>

<section class="business">
  <h2 class="section-title">Business Insurance</h2>
  <svg class="abs tree" viewBox="0 0 1200 531" aria-hidden="true">
    <g stroke="#777" stroke-dasharray="2 3" fill="none">
      <path d="M600 190V231M229 231H961M229 231V290M366 231V290M516 231V290M671 231V290M821 231V290M961 231V290"/>
    </g>
    <g fill="#777"><circle cx="229" cy="293" r="1.5"/><circle cx="366" cy="293" r="1.5"/><circle cx="516" cy="293" r="1.5"/><circle cx="671" cy="293" r="1.5"/><circle cx="821" cy="293" r="1.5"/><circle cx="961" cy="293" r="1.5"/></g>
  </svg>
  <div class="cover" style="left:159px"><div class="ring"><i></i></div>Commercial<br>Auto</div>
  <div class="cover" style="left:296px"><div class="ring"><i></i></div>Employment<br>Practice Liability<br>Insurance</div>
  <div class="cover active" style="left:446px"><div class="ring"><i></i></div>General Liability<br>Insurance</div>
  <div class="cover" style="left:601px"><div class="ring"><i></i></div>Professional<br>Liability Insurance</div>
  <div class="cover" style="left:751px"><div class="ring"><i></i></div>Property<br>Insurance</div>
  <div class="cover" style="left:891px"><div class="ring"><i></i></div>Workers<br>Compensation<br>Insurance</div>
</section>

<section class="industries">
  <div class="photo" role="img" aria-label="Smiling businessman in a blazer holding an open laptop"></div>
  <h2>Industries We Serve</h2>
  <div class="abs ind-tab"></div>
  <ul class="ind-list">
    <li class="first" style="left:636px;top:150px">Construction</li>
    <li style="left:636px;top:198px">Janitorial</li>
    <li style="left:636px;top:224px">Landscapers</li>
    <li style="left:636px;top:251px">Manufacturing Companies</li>
    <li style="left:636px;top:315px">Community Care Facilities</li>
    <li style="left:636px;top:341px">Home Health Agencies</li>
    <li style="left:636px;top:368px">Hospice</li>
    <li style="left:636px;top:395px">Nursing Homes</li>
    <li style="left:884px;top:150px">Restaurants</li>
    <li style="left:884px;top:175px">Towing</li>
    <li style="left:884px;top:202px">Trucking</li>
  </ul>
  <div class="abs ind-head">Healthcare Industry</div>
</section>

<section class="risk">
  <h2 class="section-title">Risk Management</h2>
  <div class="risk-block" style="left:183px;top:270px">
    <div class="badge"><i></i></div>
    <h3>Claims Management</h3>
    <p>Our approach to claims management involves close collaboration with clients. We ensure they grasp the process and receive the necessary support for effective claim filing and management.</p>
    <div class="more">&rsaquo;</div>
  </div>
  <div class="green-corner" style="left:643px;top:250px;width:383px;height:353px"></div>
  <div class="photo" style="left:623px;top:227px;width:381px;height:353px;background:linear-gradient(150deg,#d8d2c8,#8d8578 50%,#3f3a36)" role="img" aria-label="Colleagues gathered around a laptop in an office"></div>
  <div class="green-corner" style="left:165px;top:614px;width:383px;height:353px"></div>
  <div class="photo" style="left:187px;top:591px;width:381px;height:353px;background:linear-gradient(150deg,#6f7580,#c9ccd2 50%,#3a3e48)" role="img" aria-label="Hands reviewing printed charts on a desk"></div>
  <div class="risk-block" style="left:633px;top:650px">
    <div class="badge"><i></i></div>
    <h3>Compliance And Risk<br>Management</h3>
    <p>Effective risk management is crucial in today's landscape, where auto insurance rates are soaring, EPLI claims are on the rise, and businesses face escalating liabilities.</p>
    <div class="more">&rsaquo;</div>
  </div>
</section>

<section class="quote">
  <div class="photo" role="img" aria-label="Team of professionals meeting around a table"></div>
  <h2>Request a Quote</h2>
  <p>Secure your peace of mind today – click here to get a personalized insurance quote and protect what matters most.</p>
  <div class="abs field">Email</div>
  <span class="abs btn">Submit</span>
</section>

<section class="about">
  <div class="photo back" role="img" aria-label="Two businessmen in suits talking"></div>
  <div class="photo front" role="img" aria-label="Smiling couple seated at a table"></div>
  <h2>About Us</h2>
  <div class="abs copy">
    <p>Brookvale Insurance Services stands as a full-service insurance brokerage committed to unparalleled service and exceptional value. Our commitment extends to providing top-tier insurance products and resources, complemented by approachable and knowledgeable agents dedicated to delivering unparalleled customer service and ensuring client satisfaction. From personal to professional services, we offer a broad spectrum of high-quality insurance coverage, with specialized experts in each domain to meet your unique needs. Trust us for a seamless experience that prioritizes your peace of mind.</p>
    <p>At the core of our mission is an unwavering commitment to deliver unparalleled expertise, value, and service to our customers. In the intricate landscape of the insurance industry, our role as brokers is to guide our clients through the complexity of the marketplace, ensuring they find tailored solutions that precisely meet their needs.</p>
  </div>
  <span class="abs btn">Read More</span>
</section>

<section class="contact">
  <div class="abs dark-band"></div>
  <h2 class="section-title">Get In Touch</h2>
  <p class="sub">Contact us through our contact form and we'll get back to you as soon as we can.</p>
  <div class="photo" role="img" aria-label="Businesswoman on a phone call at her desk"></div>
  <form class="abs form-card">
    <h3>Send Us A Message</h3>
    <div class="row"><div class="in">First Name</div><div class="in">Last Name</div></div>
    <div class="row"><div class="in">Email</div><div class="in">Phone</div></div>
    <div class="row"><div class="in msg">Message</div></div>
    <span class="btn">Submit</span>
  </form>
</section>

<footer class="site-footer">
  <div class="abs footer-brand" style="top:4468px"><span class="dot"></span>BROOKVALE</div>
  <div class="abs footer-tag" style="top:4522px">INSURANCE SERVICES</div>
  <p class="abs footer-about" style="top:4550px">Brookvale Insurance Services stands as a full-service insurance brokerage committed to unparalleled service and exceptional value.</p>
  <div class="abs footer-social" style="top:4647px"><i></i><i></i><i></i><i></i></div>

  <div class="fcol" style="left:448px;top:4476px">
    <h4>HOME</h4>
    <ul><li>Home</li><li>Business Insurance</li><li>Industries We Serve</li><li>Risk Management</li><li>Request a Quote</li><li>About Us</li><li>Contact Us</li></ul>
  </div>
  <div class="fcol" style="left:654px;top:4476px;width:220px">
    <h4>CONTACT US</h4>
    <div class="contact-item"><svg width="12" height="12" viewBox="0 0 24 24"><path fill="#2a9a47" d="M6.6 10.8a15 15 0 0 0 6.6 6.6l2.2-2.2c.3-.3.7-.4 1-.2 1.1.4 2.3.6 3.6.6.6 0 1 .4 1 1V20c0 .6-.4 1-1 1A17 17 0 0 1 3 4c0-.6.4-1 1-1h3.5c.6 0 1 .4 1 1 0 1.3.2 2.5.6 3.6.1.3 0 .7-.2 1z"/></svg><div><b>Call Us :</b>(818) 555-0193</div></div>
    <div class="contact-item"><svg width="12" height="10" viewBox="0 0 24 18"><rect width="24" height="18" rx="2" fill="#2a9a47"/><path d="M1 2l11 8 11-8" stroke="#15152d" stroke-width="2" fill="none"/></svg><div><b>Email Us :</b>contact@brookvaleins.com</div></div>
    <div class="contact-item"><svg width="10" height="14" viewBox="0 0 20 28"><path fill="#2a9a47" d="M10 0a10 10 0 0 0-10 10c0 7.5 10 18 10 18s10-10.5 10-18A10 10 0 0 0 10 0zm0 14a4 4 0 1 1 0-8 4 4 0 0 1 0 8z"/></svg><div><b>Location :</b>7816 Marlowe Ave Unit D,<br>Studio City Ca 91627</div></div>
  </div>
  <div class="fcol" style="left:902px;top:4476px">
    <h4>NEWSLETTER</h4>
    <div class="news-input">Enter Your Email</div>
    <div class="btn news-btn">Submit</div>
  </div>
  <div class="abs copyright">© Copyright 2024 - Brookvale Insurance</div>
  <div class="abs terms">License And Subscription Terms</div>
</footer>

</body>
</html>
```